Marwick Law Letterhead

We need a new letterhead design for a Law Firm. The address for the law firm is 4175 Calloway Avenue, Suite 200, Houston, Texas 77046. Phone Number: 832-614-2093; Fax Number: 832-307-1546. The logo is uploaded to the project.

```html
<!DOCTYPE html>
<html lang="en">
<head>
<meta charset="utf-8">
<title>Marwick Law Letterhead</title>
<link href="https://fonts.googleapis.com/css2?family=Montserrat:wght@400&display=swap" rel="stylesheet">
<style>
  :root {
    --navy: #1b2f63;
    --red: #c8171f;
    --ink: #2a2a2a;
    --paper: #ffffff;
    --backdrop: #e9eaec;
  }
  * { box-sizing: border-box; margin: 0; padding: 0; }
  html, body { width: 1200px; height: 874px; overflow: hidden; }
  body {
    background: var(--backdrop);
    font-family: "Montserrat", Arial, sans-serif;
    color: var(--ink);
    position: relative;
  }
  .letterhead {
    position: absolute;
    left: 310px;
    top: 22px;
    width: 580px;
    height: 830px;
    background: var(--paper);
    box-shadow: 0 6px 18px rgba(0,0,0,0.12);
    overflow: hidden;
  }
  .firm-contact {
    position: absolute;
    right: 44px;
    top: 44px;
    text-align: right;
    font-style: normal;
    font-size: 9.5px;
    line-height: 1.45;
  }
  .firm-contact .phone-line { display: flex; justify-content: flex-end; align-items: center; gap: 4px; }
  .firm-contact svg { width: 8px; height: 8px; fill: var(--red); }
  .brand {
    position: absolute;
    left: 44px;
    top: 126px;
    display: flex;
    align-items: center;
    gap: 10px;
  }
  .brand-mark { width: 22px; height: 22px; background: var(--navy); }
  .brand-name {
    font-family: "Montserrat", Arial, sans-serif;
    font-weight: 400;
    font-size: 24px;
    line-height: 1;
    color: var(--navy);
  }
  .letter {
    position: absolute;
    left: 120px;
    top: 215px;
    width: 416px;
    font-size: 9px;
    line-height: 1.65;
  }
  .recipient { margin-bottom: 16px; }
  .letter p { margin-bottom: 16px; }
  .signature-area {
    width: 130px;
    height: 46px;
    margin-top: 8px;
    background: linear-gradient(90deg, #f1f1f1, #e4e4e4);
  }
  .footer-wave {
    position: absolute;
    left: 0;
    bottom: 0;
    width: 580px;
    height: 220px;
  }
</style>
</head>
<body>
  <main class="letterhead">
    <address class="firm-contact">
      <div>4175 Calloway Avenue</div>
      <div>Suite 200, Houston, Texas 77046</div>
      <div class="phone-line">832-614-2093
        <svg viewBox="0 0 10 10"><path d="M1 3 Q5 0 9 3 L8 5 L6.5 4 L6.5 3 Q5 2.5 3.5 3 L3.5 4 L2 5 Z M2 6 H8 V9 H2 Z"/></svg>
      </div>
      <div class="phone-line">832-307-1546
        <svg viewBox="0 0 10 10"><path d="M3 0 H7 V3 H3 Z M1 3.5 H9 V8 H7.5 V6 H2.5 V8 H1 Z M3 6.5 H7 V10 H3 Z"/></svg>
      </div>
    </address>

    <div class="brand">
      <span class="brand-mark"></span>
      <span class="brand-name">Marwick Law</span>
    </div>

    <section class="letter">
      <div class="recipient">
        <div>Mr/s</div>
        <div>First Name and Last Name</div>
        <div>Company Name</div>
        <div>Address</div>
      </div>
      <p>Lorem Ipsum is simply dummy text of the printing and typesetting industry. Lorem Ipsum has been the industry's standard dummy text ever since the 1500s, when an unknown printer took a galley of type and scrambled it to make a type specimen book. It has survived not only five centuries, but also the leap into electronic typesetting, remaining essentially unchanged. It was popularised in the 1960s with the release of Letraset sheets containing Lorem Ipsum passages.</p>
      <p>The standard chunk of Lorem Ipsum used since the 1500s is reproduced below for those interested. Sections 1.10.32 and 1.10.33 from "de Finibus Bonorum et Malorum" by Cicero are also reproduced in their exact original form, accompanied by English versions from the 1914 translation by H. Rackham. Lorem ipsum dolor sit amet, consectetur adipiscing elit, sed do eiusmod tempor incididunt ut labore et dolore magna aliqua.</p>
      <p>It is a long established fact that a reader will be distracted by the readable content of a page when looking at its layout. The point of using Lorem Ipsum is that it has a more-or-less normal distribution of letters, as opposed to using 'Content here, content here', making it look like readable English. Many desktop publishing packages and web page editors now.</p>
      <div class="sign-off">Your Sincerely,</div>
      <div class="signature-area" role="img" aria-label="Handwritten signature"></div>
    </section>

    <svg class="footer-wave" viewBox="0 0 580 220" preserveAspectRatio="none" aria-hidden="true">
      <path d="M0 220 C140 170 300 150 420 110 C500 82 555 45 580 0 L580 220 Z" fill="var(--red)"/>
      <path d="M8 220 C146 174 304 156 424 117 C503 90 557 55 580 12 L580 220 Z" fill="var(--paper)"/>
      <path d="M18 220 C152 180 308 163 428 125 C506 99 559 66 580 24 L580 220 Z" fill="var(--navy)"/>
    </svg>
  </main>
</body>
</html>
```